Want a DL Flyer designed for mailout, with the following info. Please see the website www.ledgerbrightco.com.au for any other info.
Content:
EVERYTHING YOU NEED FROM AN ACCOUNTANT
(tick) Value for money
(tick) Mobile visits to your farm or business
(tick) Fixed Fees Agreed Upfront
(tick) Advice tailored to your circumstances
(tick) Help to grow your business
(tick) Talk directly to your accountant, the person who knows you
(tick) Small business & Primary Producer Specialists
+ MORE.......TALLYWELL GROUP. YOU'RE MORE THAN A NUMBER WITH US.
Director: Gordon Pellew CPA | Associate: Soraya Finch CPA
Call (07) 4519 2386 www.ledgerbrightco.com.au PO Box 827 Dalby Qld 4405

```html
<!DOCTYPE html>
<html lang="en">
<head>
<meta charset="utf-8">
<title>Tallywell Group DL Flyer</title>
<link href="https://fonts.googleapis.com/css2?family=Fira+Sans+Condensed:wght@500;600;700&family=Lato:wght@400;700&display=swap" rel="stylesheet">
<style>
:root{
  --red:#e3343a;
  --blue:#17789c;
  --ink:#3c3c3c;
  --grey:#7a7c7f;
  --band:#d4d6d8;
  --stage:#a9abae;
  --paper:#ffffff;
}
*{margin:0;padding:0;box-sizing:border-box}
html,body{width:928px;height:1200px;overflow:hidden;background:var(--stage)}
.flyer{position:absolute;left:164px;top:0;width:600px;height:1200px;background:var(--paper);overflow:hidden;font-family:"Lato",sans-serif;color:var(--ink)}
.hero{position:absolute;left:0;top:0;width:600px;height:700px}
.brand{position:absolute;left:40px;top:126px;display:flex;align-items:center;gap:12px}
.brand-mark{width:26px;height:26px;background:var(--red)}
.brand-name{font-family:"Fira Sans Condensed",sans-serif;font-weight:600;font-size:36px;color:var(--red);letter-spacing:.2px}
.headline{position:absolute;left:111px;top:588px;font-family:"Fira Sans Condensed",sans-serif;font-weight:700;font-size:37px;line-height:43px;color:var(--red);text-transform:uppercase}
.headline .accent{color:var(--blue)}
.benefits{position:absolute;left:134px;top:685px;width:420px;list-style:none;font-size:20px;line-height:25px}
.benefits li{position:relative;padding-left:29px;margin-bottom:7px}
.benefits svg{position:absolute;left:0;top:5px;width:15px;height:15px}
.tagline{position:absolute;left:0;width:600px;text-align:center;font-family:"Fira Sans Condensed",sans-serif;font-weight:700}
.tagline-more{top:982px;font-size:24px;letter-spacing:3px;color:var(--grey)}
.tagline-more .firm{color:var(--red)}
.tagline-main{top:1012px;font-size:30px;color:var(--blue);letter-spacing:.3px}
.team{position:absolute;left:0;top:1059px;width:600px;height:69px;background:var(--band);display:flex}
.member{width:300px;padding:10px 0 0 58px}
.member + .member{border-left:1px solid #9c9ea1;padding-left:52px;margin:8px 0;padding-top:2px}
.member-name{font-family:"Fira Sans Condensed",sans-serif;font-weight:500;font-size:23px;line-height:26px;color:var(--red)}
.member-role{font-size:14px;line-height:16px;color:#222}
.contact{position:absolute;left:0;top:1128px;width:600px;height:72px}
.call{position:absolute;left:42px;top:20px;font-family:"Fira Sans Condensed",sans-serif;font-weight:700;font-size:28px;color:var(--grey)}
.call .num{color:var(--red)}
.address{position:absolute;left:311px;top:14px;font-size:18px;line-height:22px;color:#222;font-weight:700}
.address span{display:block;font-weight:400}
</style>
</head>
<body>
<main class="flyer">
  <svg class="hero" viewBox="0 0 600 700" aria-hidden="false">
    <defs>
      <linearGradient id="photoTone" x1="0" y1="0" x2="1" y2="1">
        <stop offset="0" stop-color="#fbfbfa"/>
        <stop offset=".45" stop-color="#eef0f2"/>
        <stop offset=".75" stop-color="#9fb0c2"/>
        <stop offset="1" stop-color="#3a4e6c"/>
      </linearGradient>
    </defs>
    <rect x="0" y="0" width="600" height="700" fill="url(#photoTone)" role="img" aria-label="Photo of an accountant's hands working with a pen, calculator, glasses and printed charts on a bright desk"/>
    <path d="M0 573 C160 470 360 440 600 444 L600 700 L0 700 Z" fill="var(--red)"/>
    <path d="M0 671 C120 520 320 456 600 454 L600 700 L0 700 Z" fill="var(--paper)"/>
  </svg>

  <div class="brand">
    <span class="brand-mark"></span>
    <span class="brand-name">Tallywell Group</span>
  </div>

  <h1 class="headline">Everything you need<br>from <span class="accent">an accountant</span></h1>

  <ul class="benefits">
    <li><svg viewBox="0 0 15 15"><rect x="1" y="3" width="11" height="11" fill="none" stroke="#8a8c8f" stroke-width="1.4"/><path d="M3 8 L6.5 11.5 L14 2" fill="none" stroke="var(--red)" stroke-width="2"/></svg>Value for money</li>
    <li><svg viewBox="0 0 15 15"><rect x="1" y="3" width="11" height="11" fill="none" stroke="#8a8c8f" stroke-width="1.4"/><path d="M3 8 L6.5 11.5 L14 2" fill="none" stroke="var(--red)" stroke-width="2"/></svg>Mobile visits to your farm or business</li>
    <li><svg viewBox="0 0 15 15"><rect x="1" y="3" width="11" height="11" fill="none" stroke="#8a8c8f" stroke-width="1.4"/><path d="M3 8 L6.5 11.5 L14 2" fill="none" stroke="var(--red)" stroke-width="2"/></svg>Fixed Fees Agreed Upfront</li>
    <li><svg viewBox="0 0 15 15"><rect x="1" y="3" width="11" height="11" fill="none" stroke="#8a8c8f" stroke-width="1.4"/><path d="M3 8 L6.5 11.5 L14 2" fill="none" stroke="var(--red)" stroke-width="2"/></svg>Advice tailored to your circumstances</li>
    <li><svg viewBox="0 0 15 15"><rect x="1" y="3" width="11" height="11" fill="none" stroke="#8a8c8f" stroke-width="1.4"/><path d="M3 8 L6.5 11.5 L14 2" fill="none" stroke="var(--red)" stroke-width="2"/></svg>Help to grow your business</li>
    <li><svg viewBox="0 0 15 15"><rect x="1" y="3" width="11" height="11" fill="none" stroke="#8a8c8f" stroke-width="1.4"/><path d="M3 8 L6.5 11.5 L14 2" fill="none" stroke="var(--red)" stroke-width="2"/></svg>Talk directly to your accountant, the person who knows you</li>
    <li><svg viewBox="0 0 15 15"><rect x="1" y="3" width="11" height="11" fill="none" stroke="#8a8c8f" stroke-width="1.4"/><path d="M3 8 L6.5 11.5 L14 2" fill="none" stroke="var(--red)" stroke-width="2"/></svg>Small business &amp; Primary Producer Specialists</li>
  </ul>

  <p class="tagline tagline-more">+ MORE.... <span class="firm">TALLYWELL GROUP.</span></p>
  <p class="tagline tagline-main">YOU'RE MORE THAN A NUMBER WITH US.</p>

  <section class="team">
    <div class="member">
      <p class="member-name">Gordon Pellew CPA</p>
      <p class="member-role">Director</p>
    </div>
    <div class="member">
      <p class="member-name">Soraya Finch CPA</p>
      <p class="member-role">Associate</p>
    </div>
  </section>

  <footer class="contact">
    <p class="call">Call <span class="num">(07) 4519 2386</span></p>
    <p class="address">www.ledgerbrightco.com.au<span>PO Box 827 Dalby Qld 4405</span></p>
  </footer>
</main>
</body>
</html>
```